Business Card Re-Design

Consulting Company: To build a high performance organization, you need great leaders at all levels throughout your organization. The Cedar Path Talent Institute engages, inspires, and educates current and future leaders to step beyond the ordinary and deliver exceptional results. This new breed of leaders will motivate your staff to leave the safety of complacency behind and come together to build an extraordinary organization. The current trend has been to ask our people to do more with fewer resources. People have been stepping up to the challenge, but more is required to ensure success with a new work paradigm. We work with your management team to build a successful strategy that will make your organization more effective. CPTI then supports your management team by providing a comprehensive set of proven services to empower your entire organization to successfully execute new strategies.Let CPTI help you optimize your organization’s individual and team performance today!

Target Market(s)

Federal, State and Local Government / Non profit

Industry/Entity Type

Management Consulting

Contact Information for Business Card

CPTI, inc (Cedar Path Talent Institute) Optimizing Individual and Organizational Performance

Colors
fee18a
ec1f27
474747
fbf289

Requirements
Must have
• Professional and high quality feel

```html
<!DOCTYPE html>
<html lang="en">
<head>
<meta charset="utf-8">
<title>Cedar Path Talent Institute – Business Card</title>
<link href="https://fonts.googleapis.com/css2?family=Oswald:wght@500;700&family=Questrial&display=swap" rel="stylesheet">
<style>
  :root {
    --brand-red: #ec2227;
    --charcoal: #474747;
    --charcoal-deep: #141414;
    --paper: #ffffff;
  }
  html, body {
    margin: 0;
    width: 1200px;
    height: 1197px;
    overflow: hidden;
    background: var(--paper);
  }
  .canvas {
    position: relative;
    width: 1200px;
    height: 1197px;
  }
  .card {
    position: absolute;
    left: 0;
    top: 396px;
    width: 1103px;
    height: 628px;
    overflow: hidden;
  }
  .card-art {
    position: absolute;
    inset: 0;
  }
  .brand-name {
    position: absolute;
    left: 0;
    width: 462px;
    top: 340px;
    margin: 0;
    text-align: center;
    font-family: "Oswald", sans-serif;
    font-weight: 500;
    font-size: 40px;
    line-height: 42px;
    color: var(--paper);
    letter-spacing: 0.5px;
    text-transform: uppercase;
  }
  .holder {
    position: absolute;
    right: 36px;
    top: 72px;
    text-align: right;
    font-family: "Oswald", sans-serif;
    font-weight: 700;
    color: var(--paper);
    text-transform: uppercase;
  }
  .holder-name {
    margin: 0;
    font-size: 54px;
    line-height: 64px;
    letter-spacing: 0;
    white-space: nowrap;
  }
  .holder-title {
    margin: 0;
    font-size: 34px;
    line-height: 40px;
  }
  .contact {
    position: absolute;
    right: 36px;
    top: 290px;
    margin: 0;
    padding: 0;
    list-style: none;
    text-align: right;
    font-family: "Questrial", sans-serif;
    font-size: 38px;
    line-height: 51.5px;
    color: var(--paper);
  }
  .contact .web { margin-right: 12px; }
</style>
</head>
<body>
<div class="canvas">
  <section class="card">
    <svg class="card-art" viewBox="0 0 1103 628" width="1103" height="628" aria-hidden="true">
      <defs>
        <radialGradient id="darkGlow" cx="300" cy="330" r="520" gradientUnits="userSpaceOnUse">
          <stop offset="0" stop-color="#474747"/>
          <stop offset="1" stop-color="#141414"/>
        </radialGradient>
        <linearGradient id="edgeShade" x1="0" y1="0" x2="1" y2="0">
          <stop offset="0" stop-color="#000" stop-opacity="0"/>
          <stop offset="1" stop-color="#000" stop-opacity="0.45"/>
        </linearGradient>
      </defs>
      <rect class="red-field" width="1103" height="628" fill="#ec2227"/>
      <polygon class="dark-field" points="0,0 735,0 297,628 0,628" fill="url(#darkGlow)"/>
      <polygon class="dark-edge" points="640,0 735,0 297,628 220,628" fill="url(#edgeShade)"/>
      <polygon class="divider" points="735,0 762,0 324,628 297,628" fill="#ffffff"/>
      <circle class="brand-mark" cx="231" cy="176" r="137" fill="#ec2227" stroke="#ffffff" stroke-width="6"/>
    </svg>

    <h1 class="brand-name">Cedar Path Talent<br>Institute</h1>

    <div class="holder">
      <p class="holder-name">Mark T. Dale</p>
      <p class="holder-title">President / CEO</p>
    </div>

    <ul class="contact">
      <li>301-555-0142</li>
      <li>301-555-0187 (Fax)</li>
      <li>P.O. Box 3182</li>
      <li>Ridgefield, MD 20700</li>
      <li>mdale@cptiinc.com</li>
      <li class="web">www.cptiinc.com</li>
    </ul>
  </section>
</div>
</body>
</html>
```